Window Graphics for Chiropractic office

I need graphics design for my storefront windows for my chiropractic office. The city is very strict about how much of the windows can be covered. They don't allow for perforated decals at all. I will upload the specifics. The lettering and any graphics cannot occupy more than 20% of the windows. The lettering cannot be higher than 6 inches tall. The design that is need here will be submitted to a graphics design department where they design it on their software at the printing company. So it doesn't really matter here how clear the pics are etc. The design proofs I received from the printing company were very disappointing which is the reason I am requesting some designs from here. The door already has graphics on it that should match what is being designed on the window panes.
My office is spa, beachy like inside. I wouldn't mind something that exudes relaxation. I treat a lot of pregnant women and families as well as auto injuries.
Per the city, they state , "Window signs shall not exceed an aggregate area equal to 20 percent of the window on which they are located, or 9 square feet per window, whichever is less. Letter heights on window signs shall be a maximum of 6 inches."
Enclosed is the proof the printing company provided which I think is very blah. Maybe some color and small banners?
The left pane should read
Prenatal Chiropractic Care
Low Back Pain
Musculoskeletal Pelvic Pain
Sciatic Pain
Hip Pain
Children & Families
Wellness care
Sports injuries
Scoliosis
Musculoskeletal Pain
The middle Pane can be left as is in terms of what it says, except it should say call or text us at 407-829-3160
The right pane should say
Auto Injuries
Whiplash
Low Back Pain & Sciatica
Carpal Tunnel Syndrome
Plantar Fascitis/Achilles Tendinitis
Knee/Shoulder Pain
I'd like some feminine akin to what is attached with the Prenatal attachm,ent. The writing there might be too hard to read far away, but I like the gist of it. If it doesn't match the door that is no big deal. I can chage it if I really like the window pane design.

```html
<!DOCTYPE html>
<html lang="en">
<head>
<meta charset="utf-8">
<title>Seabreeze Chiropractic – Window Panes</title>
<link href="https://fonts.googleapis.com/css2?family=Great+Vibes&family=Tinos:wght@400;700&display=swap" rel="stylesheet">
<style>
  :root {
    --page: #ffffff;
    --pane: #f2f0f1;
    --ink: #111111;
    --mist-blue: #a9c3dd;
    --mist-blue-soft: rgba(150, 182, 214, 0.55);
    --warm-orange: #f4a06a;
  }
  * { margin: 0; padding: 0; box-sizing: border-box; }
  html, body {
    width: 708px; height: 1200px; overflow: hidden;
    background: var(--page);
  }
  body { position: relative; font-family: "Tinos", "Times New Roman", serif; color: var(--ink); }

  .pane { position: absolute; background: var(--pane); overflow: hidden; }
  .pane--left   { left: 66px;  top: 48px;  width: 576px; height: 387px; }
  .pane--middle { left: 176px; top: 488px; width: 357px; height: 305px; }
  .pane--right  { left: 43px;  top: 848px; width: 622px; height: 305px; }

  /* soft watercolour banners */
  .banner {
    position: absolute; height: 40px;
    background: linear-gradient(90deg, var(--mist-blue-soft) 0%, rgba(169,195,221,0.35) 55%, rgba(169,195,221,0) 100%);
    filter: blur(6px); border-radius: 20px;
  }
  .banner--prenatal { left: 6px;  top: 42px;  width: 320px; }
  .banner--families { left: 6px;  top: 212px; width: 240px; }

  .script-heading {
    position: absolute; left: 45px;
    font-family: "Great Vibes", cursive; font-weight: 400;
    font-size: 36px; line-height: 1; white-space: nowrap;
  }
  .script-heading--prenatal { top: 40px; }
  .script-heading--families { top: 210px; }

  .service-list { position: absolute; list-style: none; font-size: 19px; line-height: 24px; }
  .service-list--prenatal { left: 45px; top: 87px; }
  .service-list--families { left: 45px; top: 255px; }

  .illustration {
    position: absolute;
    background: radial-gradient(circle at 35% 40%, rgba(244,160,106,0.55) 0 14%, transparent 24%),
                radial-gradient(ellipse at 60% 60%, var(--mist-blue) 0%, rgba(169,195,221,0.4) 55%, rgba(242,240,241,0) 80%);
  }
  .illustration--prenatal { left: 297px; top: 31px; width: 253px; height: 331px; }
  .illustration--back {
    left: 291px; top: 22px; width: 300px; height: 251px;
    background: radial-gradient(circle at 62% 28%, rgba(244,160,106,0.6) 0 16%, transparent 26%),
                radial-gradient(circle at 30% 82%, rgba(244,160,106,0.6) 0 13%, transparent 22%),
                radial-gradient(ellipse at 50% 60%, #dcd8d9 0%, rgba(169,195,221,0.35) 60%, rgba(242,240,241,0) 85%);
  }

  /* contact pane */
  .contact { position: absolute; inset: 0; text-align: center; }
  .contact > * { position: absolute; left: 0; right: 0; }
  .practice-name { top: 52px; font-size: 20px; font-weight: 700; letter-spacing: 0.3px; }
  .practice-mark { top: 92px; left: 50%; right: auto; width: 14px; height: 14px; margin-left: -7px;
    border: 1px solid var(--ink); border-radius: 50%; }
  .doctor-name { top: 124px; font-size: 19px; font-weight: 700; }
  .doctor-title { top: 149px; font-size: 16px; }
  .call-line { top: 183px; font-size: 15px; }
  .phone { top: 200px; font-size: 38px; font-weight: 700; letter-spacing: -0.5px; }
  .language { top: 247px; font-size: 15px; letter-spacing: 0.3px; }

  /* injury list */
  .injury-list { position: absolute; left: 47px; top: 36px; list-style: none; font-size: 19px; }
  .injury-list li { position: relative; height: 35.3px; line-height: 24px; }
  .injury-list li.continued { padding-left: 15px; }
  .injury-list li::before {
    content: ""; position: absolute; left: -22px; top: 6px; width: 60px; height: 12px;
    background: linear-gradient(90deg, rgba(150,182,214,0.55), rgba(150,182,214,0));
    filter: blur(4px); border-radius: 6px; z-index: -1;
  }
  .injury-list li.continued::before { display: none; }
</style>
</head>
<body>

<section class="pane pane--left">
  <div class="banner banner--prenatal"></div>
  <h2 class="script-heading script-heading--prenatal">Prenatal Chiropractic Care</h2>
  <ul class="service-list service-list--prenatal">
    <li>- Low Back Pain</li>
    <li>- Musculoskeletal Pelvic Pain</li>
    <li>- Sciatic Pain</li>
    <li>- Hip Pain</li>
  </ul>
  <div class="banner banner--families"></div>
  <h2 class="script-heading script-heading--families">Children &amp; Families</h2>
  <ul class="service-list service-list--families">
    <li>- Wellness Care</li>
    <li>- Sports Injuries</li>
    <li>- Scoliosis</li>
    <li>- Musculoskeletal Pain</li>
  </ul>
  <div class="illustration illustration--prenatal" role="img" aria-label="Line illustration of a kneeling pregnant woman with spine dots and a warm glow at the low back"></div>
</section>

<section class="pane pane--middle">
  <div class="contact">
    <h1 class="practice-name">SEABREEZE CHIROPRACTIC</h1>
    <span class="practice-mark" aria-hidden="true"></span>
    <p class="doctor-name">Dr. Maren Collins, D.C.</p>
    <p class="doctor-title">Chiropractic Physician</p>
    <p class="call-line">Call or text us at</p>
    <p class="phone">407.829.3160</p>
    <p class="language">HABLAMOS ESPANOL</p>
  </div>
</section>

<section class="pane pane--right">
  <ul class="injury-list">
    <li>- Auto Injuries</li>
    <li>- Whiplash</li>
    <li>- Low Back Pain &amp; Sciatica</li>
    <li>- Carpal Tunnel Syndrome</li>
    <li>- Plantar Fascitis/</li>
    <li class="continued">Achilles Tendinitis</li>
    <li>- Knee/Shoulder/ Pain</li>
  </ul>
  <div class="illustration illustration--back" role="img" aria-label="Line illustration of a person from behind holding neck and low back, with spine dots and warm pain glows"></div>
</section>

</body>
</html>
```